BARRIER BANNER KTV

I am looking for a visual for a banner
3 meters long by 1 high.
In the same theme as the visual identity of the company.
As simple as possible without overloading

There must be the LOGO, the title VOLTARIS SERVICES TECHNIQUES

_________________________

I am looking for a visual for a banner (barrier banner)
3 meters long by 1 high.

AIR CONDITIONING HEATING VENTILATION
04 52 31 69 14

Font styles to use
Sans Serif

Colors
33b8a4
00a990
33a6d7
0493ce
3176b5
0355a3
ffffff

Requirements
Should not have
• No photo
No photo

```html
<!DOCTYPE html>
<html lang="fr">
<head>
<meta charset="utf-8">
<title>KTV – Bâche barrière</title>
<link rel="stylesheet" href="https://fonts.googleapis.com/css2?family=Oswald:wght@500;600;700&family=Open+Sans:wght@600&display=swap">
<style>
  :root {
    --page: #e4e4e4;
    --white: #ffffff;
    --ink: #2e3c47;
    --teal: #33b8a4;
    --blue: #2a8cc0;
  }
  html, body {
    margin: 0;
    width: 1084px;
    height: 1200px;
    overflow: hidden;
    background: var(--page);
  }
  .banner {
    position: absolute;
    left: 42px;
    top: 433px;
    width: 1000px;
    height: 333px;
    display: block;
    box-shadow: 0 18px 30px rgba(0,0,0,0.25);
  }
  .brand-name { font-family: "Oswald", sans-serif; font-weight: 700; fill: var(--ink); }
  .title { font-family: "Oswald", sans-serif; font-weight: 700; }
  .subtitle { font-family: "Oswald", sans-serif; font-weight: 700; fill: var(--blue); }
  .services { font-family: "Oswald", sans-serif; font-weight: 600; fill: var(--white); }
  .website { font-family: "Open Sans", sans-serif; font-weight: 600; fill: var(--white); }
  .phone-number { font-family: "Oswald", sans-serif; font-weight: 600; fill: var(--white); }
</style>
</head>
<body>
<svg class="banner" viewBox="0 0 1000 333" xmlns="http://www.w3.org/2000/svg">
  <defs>
    <linearGradient id="brandGradient" x1="0" y1="0" x2="1" y2="0">
      <stop offset="0" stop-color="#33b8a4"/>
      <stop offset="1" stop-color="#2a95c4"/>
    </linearGradient>
    <linearGradient id="phoneBand" x1="0" y1="0" x2="1" y2="0">
      <stop offset="0" stop-color="#33b8a4"/>
      <stop offset="1" stop-color="#2591bf"/>
    </linearGradient>
  </defs>

  <rect class="canvas" width="1000" height="333" fill="var(--white)"/>

  <!-- brand name -->
  <text class="brand-name" x="45" y="226" font-size="200" textLength="377" lengthAdjust="spacingAndGlyphs">KTV</text>

  <!-- title block -->
  <text class="title" x="518" y="143" font-size="104" fill="url(#brandGradient)" textLength="400" lengthAdjust="spacingAndGlyphs">VOLTARIS</text>
  <text class="subtitle" x="518" y="184" font-size="40" textLength="400" lengthAdjust="spacingAndGlyphs">SERVICES TECHNIQUES</text>

  <polygon class="services-band" points="521,196 917,196 908,229 513,229" fill="var(--ink)"/>
  <text class="services" x="536" y="220" font-size="21" textLength="366" lengthAdjust="spacingAndGlyphs">AIR CONDITIONING  |  HEATING  |  VENTILATION</text>

  <!-- footer -->
  <rect class="footer-stripe" x="0" y="325" width="480" height="8" fill="var(--teal)"/>
  <polygon class="footer-band" points="0,272 462,272 440,325 0,325" fill="var(--ink)"/>
  <polygon class="phone-band" points="474,231 1000,231 1000,333 436,333" fill="url(#phoneBand)"/>
  <polygon class="corner-block" points="948,229 1000,229 1000,333 908,333" fill="var(--ink)"/>

  <!-- website -->
  <g class="globe-icon" fill="none" stroke="var(--white)" stroke-width="1.4">
    <circle cx="48" cy="298" r="10"/>
    <ellipse cx="48" cy="298" rx="4.5" ry="10"/>
    <line x1="38" y1="298" x2="58" y2="298"/>
    <line x1="40" y1="292.5" x2="56" y2="292.5"/>
    <line x1="40" y1="303.5" x2="56" y2="303.5"/>
  </g>
  <text class="website" x="64" y="306" font-size="21" textLength="363" lengthAdjust="spacingAndGlyphs">voltaris-services-techniques.fr</text>

  <!-- phone -->
  <circle class="phone-icon-ring" cx="509" cy="295" r="26" fill="var(--ink)" stroke="var(--white)" stroke-width="3"/>
  <path class="phone-icon" d="M499 284c2-2 4-2 5 0l3 5c1 2 0 3-1 4l-2 1c1 3 4 6 7 7l1-2c1-1 2-2 4-1l5 3c2 1 2 3 0 5l-2 2c-3 2-10-1-15-6s-8-12-6-15z" fill="var(--white)"/>
  <g class="phone-waves" fill="none" stroke="var(--white)" stroke-width="1.8" stroke-linecap="round">
    <path d="M511 283a8 8 0 0 1 7 7"/>
    <path d="M512 277a14 14 0 0 1 12 12"/>
  </g>
  <text class="phone-number" x="552" y="318" font-size="58" textLength="347" lengthAdjust="spacingAndGlyphs">04-5231-6914</text>
</svg>
</body>
</html>
```